BrivaTrek Freight Services Business cards

Would like a very unique design catchy but professional for business cards. Please use log provided.Marlon WellsCeo and Founder TransCon Logistix Solutions1-888-913-3225mwells@tlsolutionsus.comwww.bfservicesco.com

```html
<!DOCTYPE html>
<html lang="en">
<head>
<meta charset="UTF-8">
<title>BrivaTrek Freight Services – Business Cards</title>
<link rel="stylesheet" href="https://fonts.googleapis.com/css2?family=Arimo:wght@400;700&display=swap">
<style>
  :root {
    --brand-blue: #1276bd;
    --brand-red: #e8212a;
    --ink-grey: #4a4a4a;
    --paper: #ffffff;
    --backdrop: #eef0f2;
  }
  * { margin: 0; padding: 0; box-sizing: border-box; }
  html, body { width: 1200px; height: 1200px; overflow: hidden; }
  body {
    background: var(--backdrop);
    font-family: "Arimo", Arial, sans-serif;
    position: relative;
  }
  .card {
    position: absolute;
    left: 170px;
    width: 860px;
    height: 491px;
    overflow: hidden;
    box-shadow: 0 6px 20px rgba(0,0,0,0.12);
  }
  .card--front { top: 82px; background: var(--brand-blue); }
  .card--back { top: 627px; background: var(--paper); }

  .wordmark {
    display: flex;
    align-items: center;
    gap: 16px;
    font-weight: 700;
    letter-spacing: 1px;
  }
  .wordmark__square { width: 26px; height: 26px; background: var(--brand-red); flex: none; }
  .card--front .wordmark {
    position: absolute;
    left: 0; right: 0; top: 50%;
    transform: translateY(-50%);
    justify-content: center;
    color: var(--paper);
    font-size: 44px;
  }

  .holder { position: absolute; left: 60px; top: 62px; }
  .holder__name { color: var(--brand-blue); font-weight: 700; font-size: 44px; }
  .holder__title { color: var(--ink-grey); font-size: 24px; margin-top: 4px; }

  .contact { position: absolute; left: 470px; top: 62px; color: var(--ink-grey); }
  .contact__company { font-weight: 700; font-size: 21px; margin-bottom: 14px; }
  .contact__row { display: flex; align-items: center; gap: 14px; font-size: 21px; color: #222; margin-bottom: 9px; }
  .contact__icon { width: 22px; height: 22px; flex: none; }

  .card--back .wordmark {
    position: absolute;
    left: 60px; top: 300px;
    color: var(--brand-blue);
    font-size: 32px;
  }
  .bands { position: absolute; left: 0; bottom: 0; width: 860px; height: 80px; }
</style>
</head>
<body>
  <section class="card card--front">
    <div class="wordmark"><span class="wordmark__square"></span>BrivaTrek Freight Services</div>
  </section>

  <section class="card card--back">
    <div class="holder">
      <div class="holder__name">Dustin Harrow</div>
      <div class="holder__title">Ceo and Founder</div>
    </div>

    <div class="contact">
      <div class="contact__company">BrivaTrek Freight Services</div>
      <div class="contact__row">
        <svg class="contact__icon" viewBox="0 0 24 24"><path d="M6.6 10.8a15 15 0 0 0 6.6 6.6l2.2-2.2c.3-.3.7-.4 1-.2 1.1.4 2.3.6 3.6.6.6 0 1 .4 1 1V20c0 .6-.4 1-1 1A17 17 0 0 1 3 4c0-.6.4-1 1-1h3.5c.6 0 1 .4 1 1 0 1.3.2 2.5.6 3.6.1.3 0 .7-.2 1z" fill="#888"/></svg>
        1-888-472-6081
      </div>
      <div class="contact__row">
        <svg class="contact__icon" viewBox="0 0 24 24"><rect x="2.5" y="5.5" width="19" height="13" fill="none" stroke="#888" stroke-width="1.5"/><path d="M2.5 5.5 12 13l9.5-7.5" fill="none" stroke="#888" stroke-width="1.5"/></svg>
        dharrow@bfservicesco.com
      </div>
      <div class="contact__row">
        <svg class="contact__icon" viewBox="0 0 24 24"><path d="M10 14a4 4 0 0 0 5.7 0l3-3a4 4 0 0 0-5.7-5.7l-1 1M14 10a4 4 0 0 0-5.7 0l-3 3a4 4 0 0 0 5.7 5.7l1-1" fill="none" stroke="#888" stroke-width="1.8" stroke-linecap="round"/></svg>
        www.bfservicesco.com
      </div>
    </div>

    <div class="wordmark"><span class="wordmark__square"></span>BrivaTrek Freight Services</div>

    <svg class="bands" viewBox="0 0 860 80" preserveAspectRatio="none">
      <polygon points="0,20 530,20 548,80 0,80" fill="var(--brand-blue)"/>
      <polygon points="540,0 860,0 860,80 562,80" fill="var(--brand-red)"/>
      <polygon points="540,0 860,0 860,22 546,22" fill="var(--paper)"/>
    </svg>
  </section>
</body>
</html>
```